Cover für ein Taschenbuch zum Thema Ruhestand gesucht!
Zielgruppe
Unsere Zielgruppe sind Senioren, bzw. Menschen im Alter 50+. Es handelt sich bei dem Buch um einen Ratgeber zum Thema 'Ruhestand'. Allerdings wird das Buch ebenso von einer jüngeren Zielgruppe gekauft, da der Ratgeber auch gerne an Eltern oder Großeltern verschenkt wird.
Aufgabenstellung
siehe Dateiupload
Format: 5,25' x 8'

```html
<!DOCTYPE html>
<html lang="de">
<head>
<meta charset="utf-8">
<title>Ihr Ruhestand – Buchcover</title>
<link rel="stylesheet" href="https://fonts.googleapis.com/css2?family=Russo+One&family=Open+Sans:wght@400;600;700&family=Montserrat:wght@700&display=swap">
<style>
  :root {
    --sky-light: #f3dcb8;
    --sky-warm: #d9a77a;
    --sea-blue: #3d6f8c;
    --sea-deep: #1f3e55;
    --shadow-dark: #1b1f24;
    --title-teal: #2f6f7c;
    --title-orange: #f0a14a;
    --navy: #14253a;
    --white: #ffffff;
    --author-orange: #f2a22e;
  }
  * { margin: 0; padding: 0; box-sizing: border-box; }
  html, body { width: 788px; height: 1200px; overflow: hidden; background: var(--white); }
  .cover { position: relative; width: 788px; height: 1200px; overflow: hidden; }
  .cover-photo {
    position: absolute; inset: 0;
    background: linear-gradient(180deg,
      var(--sky-light) 0%, #efd4b0 22%, var(--sky-warm) 34%,
      #7ea3b4 40%, var(--sea-blue) 52%, var(--sea-deep) 62%,
      #2c2e33 72%, var(--shadow-dark) 100%);
  }
  .title {
    position: absolute; top: 56px; left: 0; width: 100%;
    text-align: center; white-space: nowrap;
    font-family: "Russo One", sans-serif; font-weight: 400;
    font-size: 76px; letter-spacing: 1px; line-height: 1;
    transform: scaleY(1.15); transform-origin: top center;
    background: linear-gradient(180deg, var(--title-teal) 20%, var(--title-orange) 95%);
    -webkit-background-clip: text; background-clip: text;
    color: transparent;
  }
  .subtitle {
    position: absolute; top: 182px; left: 0; width: 100%;
    text-align: center; white-space: nowrap;
    font-family: "Open Sans", sans-serif; font-weight: 700;
    font-size: 35px; color: var(--navy);
  }
  .subtitle-rule { position: absolute; top: 226px; left: 54px; }
  .teaser-rule { position: absolute; top: 708px; left: 374px; }
  .teaser {
    position: absolute; top: 748px; left: 410px; width: 370px;
    font-family: "Open Sans", sans-serif; font-weight: 400;
    font-size: 31px; line-height: 40px; color: var(--white);
  }
  .author {
    position: absolute; top: 1068px; left: 0; width: 100%;
    text-align: center; white-space: nowrap;
    font-family: "Montserrat", sans-serif; font-weight: 700;
    font-size: 36px; letter-spacing: 12px; color: var(--author-orange);
  }
</style>
</head>
<body>
  <main class="cover">
    <div class="cover-photo" role="img" aria-label="Foto: älteres Paar von hinten auf einer Holzbank am Meer bei Sonnenuntergang, Strand mit Häusern im Hintergrund"></div>

    <h1 class="title">IHR RUHESTAND</h1>
    <p class="subtitle">Das Beste kommt immer zum Schluss!</p>
    <svg class="subtitle-rule" width="680" height="26" viewBox="0 0 680 26">
      <line x1="0" y1="13" x2="656" y2="13" stroke="#14253a" stroke-width="5"/>
      <circle cx="664" cy="13" r="9" fill="none" stroke="#14253a" stroke-width="5"/>
    </svg>

    <svg class="teaser-rule" width="24" height="260" viewBox="0 0 24 260">
      <circle cx="12" cy="12" r="8" fill="none" stroke="#ffffff" stroke-width="4"/>
      <line x1="12" y1="20" x2="12" y2="258" stroke="#ffffff" stroke-width="4"/>
    </svg>
    <p class="teaser">Die besten Strategien<br>und Tipps, mit denen<br>Sie Ihre Rentenzeit in<br>vollen Zügen<br>genießen können</p>

    <p class="author">Martin Keller</p>
  </main>
</body>
</html>
```